Food Trade Show Advertisement

One full-page advertisement sent as a high-resolution .pdf file that is 11.125" w x 14.25" h

Details on the the wording and pictures will be provided
The to include:
Company logo, product photos (to be supplied), wording (to be supplied), Booth number (to be supplied)
Colors - hot pink
Attached is the guidelines for the advertisement

```html
<!DOCTYPE html>
<html lang="en">
<head>
<meta charset="utf-8">
<title>International Food Trade Show – Bella Bean</title>
<link href="https://fonts.googleapis.com/css2?family=Montserrat:wght@500;600;700&family=Courgette&display=swap" rel="stylesheet">
<style>
  :root {
    --backdrop: #2f2f2f;
    --pink: #e8177f;
    --pink-light: #f272ac;
    --pink-deep: #d10f6d;
    --pink-shadow: #8f1450;
    --white: #ffffff;
    --paper: #eeeef0;
    --green: #5bb848;
  }
  * { margin: 0; padding: 0; box-sizing: border-box; }
  html, body {
    width: 1200px; height: 1200px; overflow: hidden;
    background: var(--backdrop);
    font-family: "Montserrat", sans-serif;
  }
  .flyer {
    position: absolute; left: 168px; top: 50px;
    width: 864px; height: 1100px; overflow: hidden;
    background: linear-gradient(155deg, var(--pink-light) 0%, var(--pink) 40%, var(--pink-light) 65%, var(--pink) 85%, var(--pink-deep) 100%);
  }
  .flyer-art { position: absolute; inset: 0; }
  .abs { position: absolute; }
  .intro {
    left: 42px; top: 560px; font-size: 37px; line-height: 44px; font-weight: 500;
    color: var(--white); letter-spacing: 0.5px;
  }
  .booth {
    left: 623px; top: 571px; width: 241px; height: 28px;
    background: var(--white); clip-path: polygon(6% 0, 100% 0, 100% 100%, 0 100%);
    color: var(--pink); font-size: 21px; font-weight: 600;
    display: flex; align-items: center; justify-content: center; padding-left: 14px;
  }
  .headline {
    left: 0; width: 864px; top: 612px; text-align: center;
    font-family: "Courgette", cursive; font-size: 104px; line-height: 120px; font-weight: 400;
    color: var(--white); text-shadow: 4px 5px 0 var(--pink-shadow);
  }
  .dates {
    left: 0; width: 864px; top: 742px; line-height: 56px; text-align: center;
    font-size: 47px; font-weight: 700; color: var(--white);
    text-shadow: 3px 3px 0 var(--pink-shadow);
  }
  .hours-row {
    left: 0; width: 864px; top: 816px; height: 43px; display: flex;
    justify-content: center; align-items: center; gap: 26px;
  }
  .hours-dot { width: 11px; height: 11px; border-radius: 50%; background: var(--white); }
  .hours {
    width: 284px; height: 43px; border-radius: 22px; background: var(--white);
    color: var(--pink); font-size: 33px; font-weight: 600;
    display: flex; align-items: center; justify-content: center;
  }
  .location {
    left: 0; width: 864px; top: 895px; line-height: 28px; text-align: center;
    font-size: 22px; font-weight: 600; color: var(--white);
  }
  .perks {
    left: 229px; width: 413px; top: 964px; text-align: center;
    font-size: 25px; font-weight: 600; color: var(--pink); line-height: 44px;
  }
  .phone {
    left: 0; width: 864px; top: 1015px; height: 44px; display: flex; justify-content: center;
    align-items: center; gap: 16px; font-size: 36px; font-weight: 600; color: var(--white);
  }
  .partner-mark {
    left: 104px; top: 982px; width: 36px; height: 36px; border-radius: 50%;
    background: var(--green);
  }
  .partner-name {
    left: 40px; top: 1036px; width: 164px; text-align: center; line-height: 20px;
    font-size: 17px; font-weight: 700; color: var(--green); letter-spacing: 2px;
  }
  .brand-name {
    left: 622px; top: 176px; width: 200px; text-align: center; line-height: 32px;
    font-size: 26px; font-weight: 700; color: var(--pink);
  }
</style>
</head>
<body>
<main class="flyer">
  <svg class="flyer-art" width="864" height="1100" viewBox="0 0 864 1100">
    <defs>
      <radialGradient id="flourGlow" cx="0.55" cy="0.45" r="0.6">
        <stop offset="0" stop-color="#f2e3c2"/>
        <stop offset="0.5" stop-color="#d9d4c8"/>
        <stop offset="0.8" stop-color="#c9c9cb"/>
        <stop offset="1" stop-color="#eeeef0"/>
      </radialGradient>
      <radialGradient id="crumbGlow" cx="0.5" cy="0.55" r="0.55">
        <stop offset="0" stop-color="#d9b26a"/>
        <stop offset="1" stop-color="#f4f4f4"/>
      </radialGradient>
    </defs>
    <!-- hero white area -->
    <path class="hero-panel" d="M0 -5 H705 C760 170 560 517 267 517 C160 517 70 470 0 400 Z" fill="var(--paper)"/>
    <path class="hero-edge" d="M705 -5 C760 170 560 517 267 517 C160 517 70 470 0 400" fill="none" stroke="var(--pink)" stroke-width="5"/>
    <ellipse role="img" aria-label="Product photo: grey cloth sack spilling faba bean flour" cx="314" cy="239" rx="255" ry="165" fill="url(#flourGlow)"/>
    <!-- brand circle -->
    <circle cx="722" cy="192" r="102" fill="var(--white)" stroke="var(--pink)" stroke-width="4"/>
    <!-- product circle -->
    <circle cx="655" cy="422" r="124" fill="#f6f6f6" stroke="var(--pink)" stroke-width="4"/>
    <ellipse role="img" aria-label="Product photo: pile of textured faba bean protein crumbs" cx="655" cy="432" rx="92" ry="40" fill="url(#crumbGlow)"/>
    <!-- location pin icon -->
    <g transform="translate(432,884)" fill="none" stroke="var(--white)" stroke-width="2">
      <circle r="15"/>
      <path d="M0 7 C-6 0 -6 -3 -6 -4 A6 6 0 0 1 6 -4 C6 -3 6 0 0 7 Z"/>
      <circle cy="-4" r="2"/>
    </g>
    <!-- ribbon -->
    <polygon points="229,963 642,963 623,986 642,1009 229,1009 248,986" fill="var(--white)"/>
  </svg>

  <div class="abs brand-name">Bella Bean</div>

  <p class="abs intro">International</p>
  <div class="abs booth">Booth No: 123</div>
  <h1 class="abs headline">Food Trade Show</h1>
  <p class="abs dates">20th June - 27th June</p>
  <div class="abs hours-row">
    <span class="hours-dot"></span>
    <span class="hours">10 am - 9 pm</span>
    <span class="hours-dot"></span>
  </div>
  <p class="abs location">Place Your Location Here</p>
  <p class="abs perks">Free Entry - Free Parking</p>
  <div class="abs phone">
    <svg width="34" height="34" viewBox="0 0 34 34" fill="none" stroke="var(--white)" stroke-width="2">
      <circle cx="17" cy="17" r="15"/>
      <path d="M12 10 l3 0 l1.5 4 l-2 1.5 a9 9 0 0 0 4 4 l1.5 -2 l4 1.5 l0 3 a2 2 0 0 1 -2 2 a13 13 0 0 1 -12 -12 a2 2 0 0 1 2 -2 Z" fill="var(--white)" stroke="none"/>
    </svg>
    <span>123 123 123</span>
  </div>

  <div class="abs partner-mark"></div>
  <div class="abs partner-name">MEADOWFIELD</div>
</main>
</body>
</html>
```